Dune Air & Plus business card

I need an awesome, double-sided business card designed with our new logo. I would like the one side black with the colored logo, and the back side is all yours. I'd like to see horizontal and vertical layouts. Get creative! Thank you.

Target Market(s)

HVAC, Heating and Cooling in Phoenix, AZ

Industry/Entity Type

HVAC

Contact Information for Business Card

We need our new logo on the card. Tom Harker, (623) 555-0142, tom@trydunesair.com, www.trydunesair.com, ROC 514273

```html
<!DOCTYPE html>
<html lang="en">
<head>
<meta charset="utf-8">
<title>Dune Air &amp; Plus — Business Card</title>
<link rel="stylesheet" href="https://fonts.googleapis.com/css2?family=Archivo+Black&family=Archivo:wght@500;600&display=swap">
<style>
  :root {
    --backdrop: #8a8f96;
    --card-light: #e6e5e8;
    --card-dark: #050608;
    --ink: #111114;
    --brand-orange: #e8792a;
    --brand-blue: #1f6fc0;
  }
  * { margin: 0; padding: 0; box-sizing: border-box; }
  html, body {
    width: 1200px;
    height: 1101px;
    overflow: hidden;
    background: var(--backdrop);
  }
  .stage {
    position: relative;
    width: 1200px;
    height: 1101px;
  }
  .card {
    position: absolute;
    width: 302px;
    height: 534px;
  }
  .card--front {
    left: 246px;
    top: 266px;
    background: var(--card-light);
    color: var(--ink);
  }
  .card--back {
    left: 641px;
    top: 265px;
    background: var(--card-dark);
    display: flex;
    align-items: center;
    justify-content: center;
  }
  .holder-name {
    position: absolute;
    top: 70px;
    width: 100%;
    text-align: center;
    font-family: "Archivo Black", sans-serif;
    font-size: 29px;
    line-height: 34px;
    letter-spacing: 1.5px;
    text-transform: uppercase;
  }
  .license {
    position: absolute;
    left: 151px;
    top: 270px;
    transform: translate(-50%, -50%) rotate(-90deg);
    white-space: nowrap;
    font-family: "Archivo", sans-serif;
    font-weight: 600;
    font-size: 14px;
    letter-spacing: 3px;
  }
  .contact {
    position: absolute;
    top: 414px;
    width: 100%;
    list-style: none;
    text-align: center;
    font-family: "Archivo", sans-serif;
    font-weight: 600;
    font-size: 12px;
    line-height: 22px;
    letter-spacing: 1.6px;
    text-transform: uppercase;
  }
  .contact .phone { font-size: 14px; letter-spacing: 2px; }
  .brand {
    display: flex;
    align-items: center;
    gap: 12px;
  }
  .brand-dot {
    width: 22px;
    height: 22px;
    border-radius: 50%;
    background: var(--brand-blue);
    flex: none;
  }
  .brand-name {
    font-family: "Archivo Black", sans-serif;
    font-size: 24px;
    line-height: 28px;
    letter-spacing: 1px;
    color: var(--brand-orange);
    text-transform: uppercase;
  }
</style>
</head>
<body>
  <main class="stage">
    <section class="card card--front" aria-label="Card front">
      <h1 class="holder-name">Tom<br>Harker</h1>
      <p class="license">ROC 514273</p>
      <ul class="contact">
        <li class="phone">(623) 555-0142</li>
        <li class="email">tom@trydunesair.com</li>
        <li class="web">trydunesair.com</li>
      </ul>
    </section>
    <section class="card card--back" aria-label="Card back">
      <div class="brand">
        <span class="brand-dot"></span>
        <span class="brand-name">Dune Air<br>&amp; Plus</span>
      </div>
    </section>
  </main>
</body>
</html>
```